New business card for UK roofing company

We are Brindmore Roofing and we need a business card design for our staff.

We offer the following services:

- New roofs
- General roof repairs
- Drone surveys
- Single ply roofing
- Steel cladding
- Asbestos removal
- Electronic leak detection

I have attached our logo. I have also attached example branding printed to our vans. The business card should fit in with the style of our branding.

The business card should have the following information;

Address:
Unit 17c Wendlecroft Farm
Wendlecroft Lane
Hatchington
CM4 9QD

Telephone: 020 7946 0372
24 Hour: 0800 612 4479

Email: ray@brindmoreroofing.example
Mobile: 07700981234
Name: Ray Tunstead
Website: www.brindmoreroofing.example

The business card will be printed in Spot UV, see here: https://www.kestaprint.example/business-cards/spot-uv/

If you need anymore info, please let me know,

```html
<!DOCTYPE html>
<html lang="en">
<head>
<meta charset="utf-8">
<title>Brindmore Roofing – Business Card</title>
<link rel="stylesheet" href="https://fonts.googleapis.com/css2?family=Montserrat:wght@600;700&family=Open+Sans:wght@400;600&display=swap">
<style>
  :root {
    --bg: #e9edf1;
    --card-white: #ffffff;
    --brand-navy: #1f4f86;
    --brand-sky: #1aa3dc;
    --band-blue: #3f6a96;
    --ink-white: #ffffff;
    --shadow: rgba(20, 40, 70, 0.18);
  }
  * { box-sizing: border-box; margin: 0; padding: 0; }
  html, body { width: 1200px; height: 646px; overflow: hidden; }
  body {
    background: var(--bg);
    position: relative;
    font-family: "Open Sans", Arial, sans-serif;
  }
  .card {
    position: absolute;
    top: 168px;
    width: 540px;
    height: 309px;
    background: var(--card-white);
    box-shadow: 0 10px 28px var(--shadow);
    overflow: hidden;
  }
  .card--front { left: 40px; }
  .card--back { left: 620px; }

  /* Front */
  .brand {
    position: absolute;
    display: flex;
    align-items: center;
    gap: 10px;
    font-family: "Montserrat", Arial, sans-serif;
    font-weight: 700;
    color: var(--brand-sky);
    letter-spacing: -0.5px;
  }
  .brand__dot {
    border-radius: 50%;
    background: var(--brand-navy);
    flex: none;
  }
  .card--front .brand { left: 0; right: 0; top: 42px; justify-content: center; font-size: 34px; }
  .card--front .brand__dot { width: 34px; height: 34px; }
  .services {
    position: absolute;
    left: 52px; right: 40px; top: 120px;
    font-family: "Montserrat", Arial, sans-serif;
    font-weight: 600;
    color: var(--brand-navy);
  }
  .services__intro { font-size: 17px; text-align: center; margin-bottom: 14px; }
  .services__cols { display: flex; justify-content: space-between; }
  .services__list { list-style: none; font-size: 16px; line-height: 1.55; }

  /* Back */
  .card__art { position: absolute; inset: 0; }
  .card--back .brand { left: 18px; top: 26px; font-size: 19px; gap: 7px; }
  .card--back .brand__dot { width: 22px; height: 22px; }
  .holder {
    position: absolute;
    left: 282px; top: 38px; width: 238px;
    font-family: "Montserrat", Arial, sans-serif;
    font-weight: 700;
    font-size: 25px;
    letter-spacing: 1.5px;
    color: var(--ink-white);
    padding-bottom: 8px;
    border-bottom: 1.5px solid var(--ink-white);
  }
  .contact {
    position: absolute;
    display: flex;
    align-items: center;
    gap: 12px;
    color: var(--ink-white);
    font-size: 12px;
    line-height: 1.4;
  }
  .contact svg { flex: none; fill: var(--ink-white); }
  .contact--address { left: 292px; top: 108px; }
  .contact--phones { left: 292px; top: 172px; }
  .contact--mobile { left: 26px; top: 212px; }
  .contact--email { left: 26px; top: 242px; }
  .contact--web { left: 26px; top: 272px; }
</style>
</head>
<body>

<section class="card card--front" aria-label="Business card front">
  <div class="brand"><span class="brand__dot"></span>brindmoreroofing</div>
  <div class="services">
    <p class="services__intro">We offer the following services:</p>
    <div class="services__cols">
      <ul class="services__list">
        <li>- New roofs</li>
        <li>- General roof repairs</li>
        <li>- Drone surveys</li>
        <li>- Electronic leak detection</li>
      </ul>
      <ul class="services__list">
        <li>- Single ply roofing</li>
        <li>- Steel cladding</li>
        <li>- Asbestos removal</li>
      </ul>
    </div>
  </div>
</section>

<section class="card card--back" aria-label="Business card back">
  <svg class="card__art" width="540" height="309" viewBox="0 0 540 309" aria-hidden="true">
    <rect width="540" height="309" fill="var(--band-blue)"/>
    <polygon points="0,0 330,0 0,200" fill="var(--card-white)"/>
    <polygon points="348,0 358,0 0,217 0,211" fill="var(--card-white)"/>
  </svg>

  <div class="brand"><span class="brand__dot"></span>brindmoreroofing</div>

  <h1 class="holder">RAY TUNSTEAD</h1>

  <div class="contact contact--address">
    <svg width="26" height="26" viewBox="0 0 24 24"><path d="M12 2 1 12h3v10h6v-6h4v6h6V12h3z"/></svg>
    <span>Unit 17c Wendlecroft Farm<br>Wendlecroft Lane, Hatchington<br>CM4 9QD</span>
  </div>

  <div class="contact contact--phones">
    <svg width="26" height="26" viewBox="0 0 24 24"><path d="M6.6 10.8a15 15 0 0 0 6.6 6.6l2.2-2.2a1 1 0 0 1 1-.25 11.4 11.4 0 0 0 3.6.57 1 1 0 0 1 1 1V20a1 1 0 0 1-1 1A17 17 0 0 1 3 4a1 1 0 0 1 1-1h3.5a1 1 0 0 1 1 1c0 1.25.2 2.45.57 3.57a1 1 0 0 1-.25 1z"/></svg>
    <span>020 7946 0372<br>0800 612 4479 ( 24HOURS )</span>
  </div>

  <div class="contact contact--mobile">
    <svg width="20" height="24" viewBox="0 0 20 24"><path d="M5 1h10a2 2 0 0 1 2 2v18a2 2 0 0 1-2 2H5a2 2 0 0 1-2-2V3a2 2 0 0 1 2-2zm0 3v14h10V4zm5 15.5a1 1 0 1 0 0 2 1 1 0 0 0 0-2z"/></svg>
    <span>07700981234</span>
  </div>

  <div class="contact contact--email">
    <svg width="22" height="16" viewBox="0 0 22 16"><path d="M0 0h22v16H0zm2 2v.4l9 6.4 9-6.4V2zm0 2.8V14h18V4.8l-9 6.4z"/></svg>
    <span>ray@brindmoreroofing.example</span>
  </div>

  <div class="contact contact--web">
    <svg width="22" height="22" viewBox="0 0 24 24"><path d="M12 1a11 11 0 1 0 0 22 11 11 0 0 0 0-22zm7.9 10h-3.4a16 16 0 0 0-1.4-6.9A9 9 0 0 1 19.9 11zM12 3.1c1 1.3 2.3 4 2.5 7.9h-5C9.7 7.1 11 4.4 12 3.1zM8.9 4.1A16 16 0 0 0 7.5 11H4.1a9 9 0 0 1 4.8-6.9zM4.1 13h3.4a16 16 0 0 0 1.4 6.9A9 9 0 0 1 4.1 13zm7.9 7.9c-1-1.3-2.3-4-2.5-7.9h5c-.2 3.9-1.5 6.6-2.5 7.9zm3.1-1a16 16 0 0 0 1.4-6.9h3.4a9 9 0 0 1-4.8 6.9z"/></svg>
    <span>www.brindmoreroofing.example</span>
  </div>
</section>

</body>
</html>
```